Copyright Registration Service Website

Rightsbloomery.com (site can be accessed) is a website that will enable artists, photographers, writers, sculptors, musicians and other creative persons of all media to register their works of authorship with the U.S. Hall of Registers, Filing Bureau, for a nominal fee of $99 plus filing fees (in most cases). The high points of marketing are (1) every application is reviewed by a lawyer and (2) the entire copyright process is monitored, as part of the service fee. There are 8 categories of copyrightability:
Literary Works
Dramatic Works
Musical Works
Sound Recordings
Motion Pictures
Choreographic and Pantomime Works
Photographs, Paintings and Sculptures
Architectural Works
Please look at the existing site; provide a better landing page than currently exists. In particular, the logo is in need of serious improvement. We would like it to be bright and sunny; visually pleasant and witty; and clever but not "doctoral" in presentation. Thank you for your participation.

Target Market(s)

photographers, artists, musicians, age groups of 20-50

Industry/Entity Type

Marketing

Requirements
Should not have
• stiffness

```html
<!DOCTYPE html>
<html lang="en">
<head>
<meta charset="utf-8">
<title>Rightsbloomery.com – Copyright Registration</title>
<link href="https://fonts.googleapis.com/css2?family=Open+Sans:wght@400;600;700&family=Roboto+Condensed:wght@400;700&display=swap" rel="stylesheet">
<style>
:root{
  --blue:#1a8edb;
  --blue-bright:#2a9fdc;
  --blue-line:#1588d6;
  --navy:#0f3b58;
  --ink:#222;
  --grey-text:#555;
  --nav-text:#666;
  --box-border:#d4d4d4;
  --box-fill:#f1f1f1;
  --footer:#494949;
  --white:#fff;
}
*{box-sizing:border-box;margin:0;padding:0}
html,body{width:1074px;height:1200px;overflow:hidden;background:var(--white)}
body{position:relative;font-family:"Open Sans",Arial,sans-serif;color:var(--ink)}
.abs{position:absolute}

/* top bar */
.top-rule{left:0;top:0;width:1074px;height:3px;background:var(--blue-line)}
.top-divider{left:0;top:36px;width:1074px;height:1px;background:#cfe6f6}
.social-top{left:60px;top:10px;display:flex;gap:5px}
.social-top span{width:19px;height:19px;border-radius:50%;background:var(--blue)}
.social-top span:nth-child(3){background:#d9483b}
.social-top span:nth-child(4){background:#1d6fa5}
.account-links{left:665px;top:10px;display:flex;gap:16px;font-size:13.5px;color:#333}
.cart{left:931px;top:0;width:82px;height:31px;background:var(--blue);color:var(--white);font-size:12px;display:flex;align-items:center;justify-content:center;gap:6px}

/* header */
.brand{left:60px;top:50px;display:flex;align-items:center;gap:8px}
.brand-mark{width:46px;height:46px;border:4px solid #222;border-radius:50%}
.brand-name{font-family:"Open Sans",sans-serif;font-weight:700;font-size:20px;color:#222;letter-spacing:.1px}
.main-nav{left:358px;top:58px;display:flex;align-items:center;font-size:15px;color:var(--nav-text);white-space:nowrap}
.main-nav .sep{margin:0 10px;font-size:10px;color:#999}
.main-nav .active{color:var(--blue)}

/* hero */
.hero-band{left:0;top:111px;width:1074px;height:430px;background:var(--blue)}
.hero-photo{left:60px;top:111px;width:954px;height:382px;
  background:
    radial-gradient(ellipse 180px 230px at 640px 240px,rgba(170,160,150,.55),transparent 70%),
    radial-gradient(ellipse 130px 200px at 850px 230px,rgba(120,125,135,.5),transparent 70%),
    radial-gradient(ellipse 110px 180px at 420px 260px,rgba(150,140,130,.4),transparent 70%),
    radial-gradient(ellipse 260px 120px at 300px 60px,rgba(255,255,255,.8),transparent 70%),
    linear-gradient(100deg,#eef1f4 0%,#dde2e7 35%,#cfd4d9 60%,#e6e9ec 100%)}
.hero-title{left:92px;top:212px;font-family:"Roboto Condensed",sans-serif;font-weight:700;font-size:38px;color:#111}
.hero-points{left:82px;top:271px;width:392px;background:rgba(20,20,20,.82);padding:6px 18px}
.hero-points p{font-family:"Roboto Condensed",sans-serif;font-size:23.5px;color:var(--white);line-height:38px;border-bottom:1px solid rgba(255,255,255,.35)}
.hero-points p:last-child{border-bottom:0}
.hero-btn{left:82px;top:422px;width:83px;height:28px;background:var(--navy);color:var(--white);font-size:12px;font-weight:700;display:flex;align-items:center;justify-content:center}
.hero-dots{left:868px;top:470px;display:flex;gap:4px}
.hero-dots span{width:9px;height:9px;border-radius:50%;background:var(--white)}
.hero-dots span:first-child{background:var(--navy)}

/* services */
.services{left:74px;top:493px;width:926px;height:228px;background:linear-gradient(to bottom,var(--blue) 0%,var(--blue) 45%,#cfe7f7 85%,#fff 100%);border:2px solid var(--white);border-bottom:0}
.services-title{left:104px;top:500px;font-family:"Roboto Condensed",sans-serif;font-weight:700;font-size:19px;color:var(--white);border-bottom:1px solid var(--white);padding-bottom:1px}
.svc-card{top:541px;width:205px;height:135px;border:2px solid var(--white);overflow:hidden;box-shadow:0 1px 3px rgba(0,0,0,.2)}
.svc-card .art{width:100%;height:100%}
.svc-caption{left:0;bottom:0;width:100%;height:30px;background:rgba(0,0,0,.72);color:var(--white);font-size:14px;display:flex;align-items:center;padding-left:8px}
.svc-plus{position:absolute;right:8px;bottom:6px;width:18px;height:18px}
.svc-card.open .svc-caption{height:80px;display:block;padding:6px 8px}
.svc-card.open .svc-caption b{font-weight:400;font-size:14px;display:block;margin-bottom:2px}
.svc-card.open .svc-caption small{font-size:10px;line-height:14px;display:block;width:185px}
.svc-card.open .svc-plus{top:56px;bottom:auto}
.arrow{top:574px}

/* banner */
.promise{left:60px;top:721px;width:954px;height:95px;border:4px solid var(--blue-bright);background:var(--blue-bright);padding:3px}
.promise-inner{width:100%;height:100%;border:2px solid var(--white);display:flex;flex-direction:column;align-items:center;justify-content:center;color:var(--white);font-weight:700;font-size:21px;line-height:29px}

/* features */
.feature{top:895px;height:186px;border:1px solid var(--box-border);background:var(--white);text-align:center}
.feature.shaded{background:var(--box-fill)}
.feature-tab{position:absolute;left:50%;top:-35px;margin-left:-35px;width:70px;height:70px;border-radius:50%;border:1px solid var(--box-border);border-bottom-color:transparent;background:var(--white);display:flex;align-items:flex-start;justify-content:center;padding-top:10px}
.feature.shaded .feature-tab{background:var(--box-fill)}
.feature h3{margin-top:47px;font-family:"Roboto Condensed",sans-serif;font-weight:400;font-size:19.5px;color:#222}
.feature p{margin:4px auto 0;width:200px;font-size:12.5px;line-height:19px;color:var(--grey-text)}
.feature .btn{display:inline-block;margin-top:11px;width:74px;height:24px;line-height:24px;background:var(--blue-bright);color:var(--white);font-size:12px}

/* footer */
.footer{left:0;top:1100px;width:1074px;height:100px;background:var(--footer)}
.footer-links{left:60px;top:1116px;font-size:13px;color:#ddd;display:flex;gap:10px}
.footer-links .on{color:var(--white)}
.footer-copy{left:60px;top:1160px;font-size:13px;color:#ddd}
.footer-social{left:841px;top:1148px;display:flex;gap:5px}
.footer-social span{width:25px;height:25px;background:#e9e9e9;border-radius:2px}
.footer-social span:first-child{background:#2c5e9e}
</style>
</head>
<body>

<div class="abs top-rule"></div>
<div class="abs social-top"><span></span><span></span><span></span><span></span></div>
<div class="abs account-links"><span>Wishlist</span><span>My Account</span><span>Login / Register</span></div>
<div class="abs cart">
  <svg width="12" height="15" viewBox="0 0 12 15"><path d="M1 4h10v10H1z" fill="#fff"/><path d="M3.5 4V3a2.5 2.5 0 0 1 5 0v1" fill="none" stroke="#fff" stroke-width="1.3"/></svg>
  <span>(0) Cart</span>
</div>
<div class="abs top-divider"></div>

<div class="abs brand">
  <span class="brand-mark"></span>
  <span class="brand-name">RIGHTSBLOOMERY</span>
</div>
<nav class="abs main-nav">
  <span class="active">About us</span><span class="sep">»</span>
  <span>Copyright Cateogries</span><span class="sep">»</span>
  <span>Law &amp; Statutes</span><span class="sep">»</span>
  <span>Copyright Process</span><span class="sep">»</span>
  <span>Links</span><span class="sep">»</span>
  <span>Contact</span>
</nav>

<div class="abs hero-band"></div>
<div class="abs hero-photo" role="img" aria-label="Photo of smiling business team giving thumbs up in a bright office"></div>
<div class="abs hero-title">COPYRIGHT</div>
<div class="abs hero-points">
  <p>Protect your copyright in 5 minutes!</p>
  <p>Registration $99 (most cases)</p>
  <p>Entire process is reviewed by a lawyer</p>
</div>
<div class="abs hero-btn">Read More</div>
<div class="abs hero-dots"><span></span><span></span><span></span><span></span></div>

<div class="abs services"></div>
<div class="abs services-title">Service</div>
<svg class="abs arrow" style="left:80px" width="14" height="52" viewBox="0 0 14 52"><path d="M12 2L2 26l10 24" fill="none" stroke="#cfe7f7" stroke-width="2"/></svg>
<svg class="abs arrow" style="left:980px" width="14" height="52" viewBox="0 0 14 52"><path d="M2 2l10 24L2 50" fill="none" stroke="#0f3b58" stroke-width="2"/></svg>

<div class="abs svc-card open" style="left:104px">
  <div class="art" role="img" aria-label="Photo of a woman reading among library shelves" style="background:radial-gradient(ellipse 60px 50px at 80px 50px,#e8cdb0,transparent 70%),linear-gradient(180deg,#a8452f 0%,#c98a5c 25%,#e6ddd0 45%,#b9a58f 100%)"></div>
  <div class="abs svc-caption"><b>Literary Works</b><small>Lorem ipsum dolor sit amet, consecte-tur adipiscing elit. Nullam fringilla, dui sed sollicitudin rhoncus, diam arcu</small></div>
  <svg class="svc-plus" viewBox="0 0 18 18"><path d="M9 1v16M1 9h16" stroke="#2a9fdc" stroke-width="4"/></svg>
</div>
<div class="abs svc-card" style="left:325px">
  <div class="art" role="img" aria-label="Photo of a woman with headphones at a keyboard" style="background:radial-gradient(ellipse 50px 60px at 60px 50px,#d9a58e,transparent 70%),linear-gradient(150deg,#9e1a22,#c63a3a 50%,#5b171b)"></div>
  <div class="abs svc-caption">Musical Works</div>
  <svg class="svc-plus" viewBox="0 0 18 18"><path d="M9 1v16M1 9h16" stroke="#2a9fdc" stroke-width="4"/></svg>
</div>
<div class="abs svc-card" style="left:545px">
  <div class="art" role="img" aria-label="Photo of a studio microphone" style="background:radial-gradient(ellipse 40px 60px at 45px 50px,#c8d3dd,transparent 70%),radial-gradient(ellipse 70px 50px at 150px 40px,#4c82b8,transparent 70%),linear-gradient(150deg,#0f2a4a,#2c5885 50%,#122339)"></div>
  <div class="abs svc-caption">Sound Recordings</div>
  <svg class="svc-plus" viewBox="0 0 18 18"><path d="M9 1v16M1 9h16" stroke="#2a9fdc" stroke-width="4"/></svg>
</div>
<div class="abs svc-card" style="left:765px">
  <div class="art" role="img" aria-label="Photo of a cinema hall with red seats" style="background:radial-gradient(ellipse 90px 30px at 120px 30px,#e9e4e4,transparent 70%),linear-gradient(175deg,#3e1215 0%,#6d1b20 30%,#d12a31 60%,#a31d23 100%)"></div>
  <div class="abs svc-caption">Motion Pictures</div>
  <svg class="svc-plus" viewBox="0 0 18 18"><path d="M9 1v16M1 9h16" stroke="#2a9fdc" stroke-width="4"/></svg>
</div>

<div class="abs promise">
  <div class="promise-inner">
    <span>Every Application Is Individually Filed and Monitored under Lawyer Supervision.</span>
    <span>Protect Your Intellectual Property Rights</span>
  </div>
</div>

<div class="abs feature shaded" style="left:60px;width:226px">
  <div class="feature-tab"><svg width="30" height="36" viewBox="0 0 30 36"><path d="M8 15v-5a7 7 0 0 1 14 0v5" fill="none" stroke="#1a8edb" stroke-width="3.5"/><rect x="3" y="15" width="24" height="19" rx="2" fill="#1a8edb"/><circle cx="15" cy="23" r="2.5" fill="#fff"/><rect x="14" y="24" width="2" height="5" fill="#fff"/></svg></div>
  <h3>COPYRIGHT CATEOGRIES</h3>
  <p>Lorem ipsum dolor sit amet, conse tur adi pis cinglit. neque et cursus vehicula. Sed sed</p>
  <span class="btn">Read More</span>
</div>
<div class="abs feature" style="left:304px;width:226px">
  <div class="feature-tab"><svg width="44" height="36" viewBox="0 0 44 36"><path d="M22 3v28M10 7h24M6 32h32" stroke="#1a8edb" stroke-width="3"/><path d="M10 7L4 20h12zM34 7l-6 13h12z" fill="none" stroke="#1a8edb" stroke-width="1.5"/><path d="M3 20a7 5 0 0 0 14 0zM27 20a7 5 0 0 0 14 0z" fill="#1a8edb"/></svg></div>
  <h3>LAW &amp; STATUTES</h3>
  <p>Lorem ipsum dolor sit amet, conse tur adi pis cinglit. neque et cursus vehicula. Sed sed</p>
  <span class="btn">Read More</span>
</div>
<div class="abs feature" style="left:543px;width:225px">
  <div class="feature-tab"><svg width="40" height="36" viewBox="0 0 40 36"><rect x="3" y="3" width="34" height="23" rx="1" fill="none" stroke="#1a8edb" stroke-width="3.5"/><rect x="17" y="26" width="6" height="6" fill="#1a8edb"/><rect x="11" y="31" width="18" height="3" fill="#1a8edb"/></svg></div>
  <h3>ABOUT US</h3>
  <p>Lorem ipsum dolor sit amet, conse tur adi pis cinglit. neque et cursus vehicula. Sed sed</p>
  <span class="btn">Read More</span>
</div>
<div class="abs feature" style="left:788px;width:226px">
  <div class="feature-tab"><svg width="30" height="44" viewBox="0 0 30 44"><path d="M5 12a10 10 0 1 1 15 8.5c-3 2-5 3.5-5 8v2" fill="none" stroke="#1a8edb" stroke-width="5"/><circle cx="15" cy="39" r="3.5" fill="#1a8edb"/></svg></div>
  <h3>FAQs</h3>
  <p>Lorem ipsum dolor sit amet, conse tur adi pis cinglit. neque et cursus vehicula. Sed sed</p>
  <span class="btn">Read More</span>
</div>

<footer class="abs footer"></footer>
<div class="abs footer-links">
  <span class="on">About</span><span>|</span><span>Copyright Cateogries</span><span>|</span><span>Law &amp; Statutes</span><span>|</span><span>Copyright Process</span><span>|</span><span>Links</span><span>|</span><span>Contact</span>
</div>
<div class="abs footer-copy">Copyright © 2014.&nbsp; Rightsbloomery.com. All Rights Reserved.</div>
<div class="abs footer-social"><span></span><span></span><span></span><span></span><span></span><span></span></div>

</body>
</html>
```